Mobile mechanics business card

i need a business card for my new business im a mobile mechanic who works on farm machines, ie tractors and construction machines ie bulldozers and frost protection wind machines in orchards so would like those three machines in the back ground to show the customers what i am specializing in. just go for it and suprise me!!

Target Market(s)

orchard owner, farm owners and contractors

Industry/Entity Type

Construction

Contact Information for Business Card

Rob kellaway, mobile mechanic, Ph 0274835106, Email robk.kellaway24@mailnest.example

```html
<!DOCTYPE html>
<html lang="en">
<head>
<meta charset="utf-8">
<title>Rob Kellaway Mobile Mechanic – Business Card</title>
<link rel="stylesheet" href="https://fonts.googleapis.com/css2?family=Orbitron:wght@700;900&family=Michroma&family=Jost:wght@400;500&display=swap">
<style>
  :root {
    --page-bg: #e9e6e3;
    --card-light: #ffffff;
    --card-light-shade: #e4e4e4;
    --accent-orange: #f0a020;
    --accent-orange-deep: #d9820f;
    --ink-black: #111111;
    --panel-black: #0d0e10;
    --panel-black-soft: #1e2023;
    --text-white: #f4f4f4;
    --machine-yellow: #e8c56a;
    --machine-grey: #bfbfbf;
  }
  * { box-sizing: border-box; margin: 0; padding: 0; }
  html, body { width: 1200px; height: 800px; overflow: hidden; }
  body { background: var(--page-bg); position: relative; }

  .business-card {
    position: absolute;
    left: 100px; top: 110px;
    width: 1000px; height: 580px;
    overflow: hidden;
    box-shadow: 0 12px 30px rgba(0,0,0,.25);
    background: linear-gradient(180deg, var(--card-light) 0%, var(--card-light-shade) 100%);
  }

  .machine-art {
    position: absolute;
    border-radius: 10px;
    opacity: .55;
  }
  .machine-art--tractor {
    left: 70px; top: 190px; width: 260px; height: 170px;
    background: radial-gradient(ellipse at 60% 45%, var(--machine-yellow) 0%, var(--machine-grey) 60%, transparent 85%);
  }
  .machine-art--wind-machine {
    left: 440px; top: 95px; width: 150px; height: 270px;
    background: linear-gradient(180deg, var(--machine-grey) 0%, #d6d6d6 70%, transparent 100%);
    opacity: .4;
  }
  .machine-art--loader {
    right: 20px; top: 30px; width: 320px; height: 250px;
    background: radial-gradient(ellipse at 55% 45%, var(--machine-yellow) 0%, var(--machine-grey) 60%, transparent 85%);
  }

  .brand {
    position: absolute;
    left: 235px; top: 120px;
    z-index: 2;
  }
  .brand__name {
    font-family: "Orbitron", sans-serif;
    font-weight: 900;
    font-size: 66px;
    letter-spacing: 2px;
    color: var(--accent-orange);
    text-transform: uppercase;
    line-height: 1;
    text-shadow: 2px 2px 0 #7a4a08;
  }
  .brand__role {
    font-family: "Michroma", sans-serif;
    font-size: 34px;
    letter-spacing: 9px;
    color: var(--ink-black);
    text-transform: uppercase;
    margin: 6px 0 0 40px;
    line-height: 1;
  }

  .specialty-band {
    position: absolute;
    left: 0; top: 362px;
    width: 100%; height: 30px;
    background: linear-gradient(90deg, var(--accent-orange-deep), var(--accent-orange));
    display: flex; align-items: center; justify-content: center;
    font-family: "Orbitron", sans-serif;
    font-weight: 700;
    font-size: 17px;
    letter-spacing: 8px;
    color: var(--ink-black);
    text-transform: uppercase;
  }

  .contact-panel {
    position: absolute;
    left: 0; top: 392px;
    width: 100%; height: 188px;
    background: linear-gradient(180deg, var(--panel-black-soft) 0%, var(--panel-black) 100%);
    padding: 48px 0 0 80px;
  }
  .contact-line {
    display: flex; align-items: center; gap: 16px;
    font-family: "Jost", sans-serif;
    font-weight: 500;
    font-size: 34px;
    color: var(--text-white);
    margin-bottom: 14px;
  }
  .contact-line svg { width: 34px; height: 34px; flex: none; }
</style>
</head>
<body>
  <div class="business-card">
    <div class="machine-art machine-art--tractor" role="img" aria-label="Faded photo of a yellow farm tractor"></div>
    <div class="machine-art machine-art--wind-machine" role="img" aria-label="Faded photo of an orchard frost protection wind machine"></div>
    <div class="machine-art machine-art--loader" role="img" aria-label="Faded photo of a yellow wheel loader"></div>

    <div class="brand">
      <div class="brand__name">Rob Kellaway</div>
      <div class="brand__role">Mobile Mechanic</div>
    </div>

    <div class="specialty-band">Specializing in farm &amp; construction machines</div>

    <div class="contact-panel">
      <div class="contact-line">
        <svg viewBox="0 0 24 24" aria-hidden="true"><path fill="#f0a020" d="M6.6 10.8a15.1 15.1 0 0 0 6.6 6.6l2.2-2.2a1 1 0 0 1 1-.25 11.4 11.4 0 0 0 3.6.57 1 1 0 0 1 1 1V20a1 1 0 0 1-1 1A17 17 0 0 1 3 4a1 1 0 0 1 1-1h3.5a1 1 0 0 1 1 1c0 1.25.2 2.45.57 3.57a1 1 0 0 1-.25 1z"/></svg>
        <span>0274835106</span>
      </div>
      <div class="contact-line">
        <svg viewBox="0 0 24 24" aria-hidden="true"><rect x="2" y="5" width="20" height="14" rx="2" fill="#f0a020"/><path d="M3 6l9 7 9-7" fill="none" stroke="#111" stroke-width="1.6"/></svg>
        <span>robk.kellaway24@mailnest.example</span>
      </div>
    </div>
  </div>
</body>
</html>
```